Website for Corvalind Capital, my new firm that raises money from investors to buy, build, own an...

Corvalind Capital needs a website! We are a new company with very experienced people, who invest in, own and build hotel properties, as well as apartments and other commercial real estate. We seek investors for our projects, and we provide safe, secure returns on their investment in our projects. Our new logo is designed to exhibit strength, class and security, and would like our website to continue on this theme. Our name, Corvalind, is a word-play on a Greek word “aristeia”, which means “excellence” and “a warriors finest moment of glory in war”. If you are in business, you realize that much of it is like war, with strategy and moves and opponents and competitors, and ever-changing economic conditions and threats that make business very much like war. We like to think that we are good at business (war), and so have named our company “Corvalind”, using the founders last name and the word “aristeia” combined. Another definition of "aristeia" is "performing at the peak of one's potential after a long struggle"...again, much like business in real life! The website design should exhibit financial security, smart moves, and positive growth towards a bright future.

Target Market(s)

The target market is smart and wealthy investors, with others such as brokers, cities and government agencies, lenders, sellers, partners, etc also looking at it.

Industry/Entity Type

Investment

Number of Pages Required

5+ page

Font styles to use
Sans Serif

Colors
fec214

Requirements
Must have
• Our website should have a landing page, a "about" or bio page, a projects page and a contact us page. Our new logo uses the colors black and gold, so this should be factored in to our site. The site should be simple, yet impactful and impressive. I have actually two logos, which can be mixed and interchanged in a complimentary way, each with their own unique look.
Nice to have
• I have uploaded a couple screenshots of a website i like, and the simplicity I mention.
Should not have
• The site should not be flashy or complicated or complex or "busy"

```html
<!DOCTYPE html>
<html lang="en">
<head>
<meta charset="utf-8">
<title>Corvalind Capital</title>
<link rel="stylesheet" href="https://fonts.googleapis.com/css2?family=Questrial&family=Montserrat:wght@600;700&family=Arimo&display=swap">
<style>
:root{
  --gold:#fec214;
  --gold-deep:#d99a06;
  --ink:#1d1d1d;
  --text:#2a2a2a;
  --header:#efefef;
  --mist:#e6e6e8;
  --field:#f7f9ee;
  --white:#ffffff;
  --line:#3a3a3a;
}
*{box-sizing:border-box;margin:0;padding:0}
html,body{width:1200px;height:2848px;overflow:hidden;background:var(--white)}
body{position:relative;font-family:"Questrial",sans-serif;color:var(--text)}
.abs{position:absolute}

/* header */
.site-header{left:0;top:0;width:1200px;height:129px;background:var(--header);z-index:3}
.nav-link{top:64px;font-size:25px;color:var(--ink);transform:translate(-50%,-50%);white-space:nowrap}
.logo-drop{left:0;top:0;z-index:2}
.brand{left:600px;top:84px;transform:translate(-50%,-50%);z-index:4;display:flex;align-items:center;gap:12px;font-family:"Montserrat",sans-serif;font-weight:700;font-size:30px;letter-spacing:1px;color:var(--ink);white-space:nowrap}
.brand-mark{width:16px;height:16px;background:var(--gold)}

/* hero */
.hero{left:0;top:129px;width:1200px;height:545px;background:linear-gradient(180deg,#d8d8dc 0%,#e3e3e6 45%,#dcdcdf 100%)}
.hero-title{left:0;width:1200px;top:272px;text-align:center;font-family:"Montserrat",sans-serif;font-weight:700;font-size:39px;color:var(--ink)}
.hero-copy{left:118px;width:964px;top:336px;text-align:center;font-family:"Arimo",sans-serif;font-size:18px;line-height:27.5px;color:var(--ink)}
.btn{display:flex;align-items:center;justify-content:center;border:2px solid var(--line);font-family:"Montserrat",sans-serif;font-weight:600;color:var(--ink);letter-spacing:1px}
.btn-learn{left:484px;top:501px;width:232px;height:59px;font-size:22px;background:rgba(255,255,255,.35)}
.chevron{left:566px;top:600px}

/* bio */
.bio{left:0;top:674px;width:1200px;height:633px;background:linear-gradient(180deg,#e7a912 0%,#f5b818 40%,#d38e0a 100%)}
.bio-title{left:0;width:1200px;top:796px;text-align:center;font-family:"Montserrat",sans-serif;font-weight:700;font-size:53px;color:var(--white)}
.bio-panel{left:139px;top:988px;width:923px;height:205px;background:rgba(255,255,255,.82)}
.bio-copy{left:170px;width:860px;top:1024px;text-align:center;font-family:"Arimo",sans-serif;font-size:18px;line-height:28px;color:var(--ink)}
.btn-read{left:511px;top:1158px;width:178px;height:57px;font-size:18px;background:#e9e9e9}

/* projects */
.section-title{left:0;width:1200px;text-align:center;font-family:"Montserrat",sans-serif;font-weight:700;font-size:57px;color:var(--ink)}
.projects-title{top:1342px}
.tile{width:331px;height:248px}
.tile-photo{background:linear-gradient(135deg,#8a8580,#c9c4bc)}
.project-card{left:435px;top:1456px;background:var(--gold);text-align:center;color:var(--white)}
.card-title{margin-top:20px;font-size:27px;color:#2b2b2b}
.card-rule{width:56px;height:5px;background:var(--white);margin:10px auto 18px}
.card-copy{width:272px;margin:0 auto;font-size:17px;line-height:24px;color:#3a3a3a}
.card-plus{width:38px;height:38px;background:var(--white);margin:12px auto 0;display:flex;align-items:center;justify-content:center;font-size:30px;color:#555;line-height:1}
.btn-projects{left:471px;top:2013px;width:258px;height:57px;font-size:18px;border-color:#555}

/* contact */
.contact{left:0;top:2104px;width:1200px;height:564px;background:linear-gradient(100deg,#ececed 0%,#f2f2f2 50%,#dedfe1 100%)}
.contact-title{top:2157px}
.field{background:var(--field);font-family:"Arimo",sans-serif;font-size:13px;color:#333;padding:14px 18px}
.btn-submit{left:511px;top:2520px;width:178px;height:59px;font-size:18px;border-color:#555}

/* footer */
.footer-brand{left:76px;top:2758px;display:flex;align-items:center;gap:12px;font-family:"Montserrat",sans-serif;font-weight:700;font-size:30px;color:var(--ink);letter-spacing:1px}
.footer-nav{right:70px;top:2702px;font-size:20px;color:var(--ink);white-space:nowrap;word-spacing:2px}
.footer-nav .sep{margin:0 14px}
.social{right:70px;top:2746px;display:flex;gap:26px}
.social span{width:18px;height:18px;border-radius:50%;background:#222}
.copyright{right:70px;top:2793px;font-size:15px;color:#333;white-space:nowrap}
</style>
</head>
<body>

<header class="abs site-header">
  <span class="abs nav-link" style="left:283px">Home</span>
  <span class="abs nav-link" style="left:393px">Bio</span>
  <span class="abs nav-link" style="left:835px">Projects</span>
  <span class="abs nav-link" style="left:1000px">Contact Us</span>
</header>
<svg class="abs logo-drop" width="1200" height="210" viewBox="0 0 1200 210"><polygon points="513,128 687,128 600,205" fill="#efefef"/></svg>
<div class="abs brand"><span class="brand-mark"></span>CORVALIND</div>

<section class="abs hero" role="img" aria-label="Faded city skyline with tall towers"></section>
<h1 class="abs hero-title">We seek investors for our projects</h1>
<p class="abs hero-copy">Sed ut perspiciatis unde omnis iste natus error sit voluptatem accusantium doloremque laudantium, totam rem aperiam, eaque ipsa quae ab illo inventore veritatis et quasi architecto beatae vitae dicta sunt explicabo. Nemo enim ipsam voluptatem quia voluptas sit aspernatur aut odit aut fugit, sed quia consequuntur magni dolores eos qui ratione voluptatem sequi nesciunt. Neque porro quisquam est, qui dolorem ipsum quia dolor sit amet, consectetur, adipisci velit, sed quia non numquam eius modi tempora incidunt ut labore et dolore magnam aliquam</p>
<div class="abs btn btn-learn">LEARN MORE</div>
<svg class="abs chevron" width="68" height="34" viewBox="0 0 68 34"><polyline points="2,2 34,30 66,2" fill="none" stroke="#444" stroke-width="2"/></svg>

<section class="abs bio" role="img" aria-label="Two business people shaking hands in a glass office over a golden city view"></section>
<h2 class="abs bio-title">Bio</h2>
<div class="abs bio-panel"></div>
<p class="abs bio-copy">Sed ut perspiciatis unde omnis iste natus error sit voluptatem accusantium doloremque laudantium, totam rem aperiam, eaque ipsa quae ab illo inventore veritatis et quasi architecto beatae vitae dicta sunt explicabo. Nemo enim ipsam voluptatem quia voluptas sit aspernatur aut odit aut fugit, sed quia consequuntur magni dolores eos qui ratione voluptatem sequi nesciunt.</p>
<div class="abs btn btn-read">READ MORE</div>

<h2 class="abs section-title projects-title">Projects</h2>
<div class="abs tile tile-photo" style="left:74px;top:1456px;background:linear-gradient(135deg,#6e655c,#c8bfb2)" role="img" aria-label="Modern kitchen interior"></div>
<div class="abs tile project-card">
  <div class="card-title">Project Title</div>
  <div class="card-rule"></div>
  <p class="card-copy">Sed ut perspiciatis unde omnis iste natus error sit voluptatem accusantium doloremque laudantium, totam rem aperiam,</p>
  <div class="card-plus">+</div>
</div>
<div class="abs tile tile-photo" style="left:792px;top:1456px;background:linear-gradient(90deg,#e8e4dc,#9a968f)" role="img" aria-label="Apartment building with balconies"></div>
<div class="abs tile tile-photo" style="left:74px;top:1738px;background:linear-gradient(135deg,#4b5160,#c7ccd6)" role="img" aria-label="Skyscrapers seen from below"></div>
<div class="abs tile tile-photo" style="left:435px;top:1738px;background:linear-gradient(180deg,#3c3f8f,#6a5c86 55%,#2a2a40)" role="img" aria-label="Luxury house with pool at dusk"></div>
<div class="abs tile tile-photo" style="left:792px;top:1738px;background:linear-gradient(180deg,#2b2c33,#6b5d44 60%,#1c1c22)" role="img" aria-label="Lit commercial building at night"></div>
<div class="abs btn btn-projects">VIEW MORE PROJECTS</div>

<section class="abs contact" role="img" aria-label="Faded photo of a man working at a desk by a window"></section>
<h2 class="abs section-title contact-title">Contact Us</h2>
<div class="abs field" style="left:165px;top:2265px;width:422px;height:46px">First Name</div>
<div class="abs field" style="left:613px;top:2265px;width:422px;height:46px">Last Name</div>
<div class="abs field" style="left:165px;top:2326px;width:422px;height:48px">Email</div>
<div class="abs field" style="left:613px;top:2326px;width:422px;height:48px">Phone Number</div>
<div class="abs field" style="left:165px;top:2393px;width:870px;height:98px">Message</div>
<div class="abs btn btn-submit">SUBMIT</div>

<footer>
  <div class="abs footer-brand"><span class="brand-mark"></span>CORVALIND</div>
  <div class="abs footer-nav">Home<span class="sep">|</span>Bio<span class="sep">|</span>Projects<span class="sep">|</span>Contact Us</div>
  <div class="abs social"><span></span><span></span><span></span><span></span></div>
  <div class="abs copyright">© 2018 &nbsp;&nbsp;|&nbsp;&nbsp; www.companyname.com</div>
</footer>

</body>
</html>
```